Business Cards for Retail/Sourcing Business.

We need a business cards for our company where it looks like:
TK
LM

VERTICAL, where the TK is over the LM. Then Under the TKLM would be name, address and website address. We want the P to be in the style of our original logo, which I uploaded.

Also, can we get a couple of designs with fun colors - especially for the letter head.

Target Market(s)

Old clients. Many of our clients or people we do business with are 40-50 plus. We are not an industry with many young people.

Industry/Entity Type

Business

Contact Information for Business Card

Front side is just says TKLM with name, title, address, and website below.

Font styles to use
Serif
Sans Serif
Decorative
Script

Requirements
Must have
• THE TKLM design with the P in the design of the logo
Nice to have
• Fun colors, new takes on the TKLM and any other additions that would be cool and make it pop

```html
<!DOCTYPE html>
<html lang="en">
<head>
<meta charset="utf-8">
<title>TKLM Business Card</title>
<link rel="stylesheet" href="https://fonts.googleapis.com/css2?family=Archivo+Black&family=Cardo:wght@400&display=swap">
<style>
  :root {
    --page-bg: #e9e7e3;
    --card-top: #ffffff;
    --card-bottom: #e4e4e4;
    --band: rgba(0, 0, 0, 0.07);
    --ink: #111111;
    --ink-soft: #1e1e1e;
  }
  * { box-sizing: border-box; margin: 0; padding: 0; }
  html, body {
    width: 1200px;
    height: 885px;
    overflow: hidden;
    background: var(--page-bg);
  }
  .stage {
    width: 1200px;
    height: 885px;
    display: flex;
    align-items: center;
    justify-content: center;
  }
  .card {
    position: relative;
    width: 460px;
    height: 790px;
    border-radius: 30px;
    background: linear-gradient(170deg, var(--card-top) 0%, #f3f3f3 45%, var(--card-bottom) 100%);
    box-shadow: 0 14px 34px rgba(0, 0, 0, 0.18);
    overflow: hidden;
    text-align: center;
    color: var(--ink);
  }
  .card__band {
    position: absolute;
    left: 0;
    top: 0;
    width: 100%;
    height: 100%;
  }
  .card__content {
    position: relative;
    padding-top: 70px;
  }
  .wordmark {
    font-family: "Archivo Black", "Arial Black", sans-serif;
    font-weight: 400;
    color: var(--ink);
    font-size: 150px;
    line-height: 0.86;
    letter-spacing: -2px;
  }
  .person {
    margin-top: 58px;
    font-family: "Cardo", Georgia, serif;
    color: var(--ink-soft);
  }
  .person__name {
    font-size: 38px;
    letter-spacing: 1px;
  }
  .person__title {
    margin-top: 10px;
    font-size: 21px;
    letter-spacing: 0.5px;
  }
  .contact {
    margin-top: 38px;
    font-family: "Cardo", Georgia, serif;
    font-size: 21px;
    line-height: 1.35;
    letter-spacing: 0.5px;
    color: var(--ink-soft);
    font-style: normal;
  }
  .contact__lines + .contact__lines { margin-top: 30px; }
</style>
</head>
<body>
  <main class="stage">
    <article class="card">
      <svg class="card__band" viewBox="0 0 460 790" aria-hidden="true">
        <polygon points="0,330 460,300 460,560 0,600" fill="var(--band)"/>
      </svg>
      <div class="card__content">
        <h1 class="wordmark">TK<br>LM</h1>
        <div class="person">
          <p class="person__name">Marlon Astley</p>
          <p class="person__title">Home, Sourcingclor</p>
        </div>
        <address class="contact">
          <p class="contact__lines">482 Harbor Lane Newport,<br>Rhode Island 02840 United States</p>
          <p class="contact__lines">+14015550172<br>hello@tklmtradingco.com<br>tklmtradingco.site</p>
        </address>
      </div>
    </article>
  </main>
</body>
</html>
```